Pale Thistle Annals Trilogy - new Fantasy book series

Design of front cover and spine for each book in this trilogy based on the images attached.

The titles are as follows:
Book 1 - Heron's Lantern
Book 2 - Embers of Dusk
Book 3 - Stag of Hollowmere

Author - Clive Marlowe (and he is also the illustrator of these cover images)

The book size is b-format (W X H mm: 129 x 198)

Target Market(s)

This is a fantasy series for the age group 14+ and appeals to both male and female readers

Industry/Entity Type

Publishing

Requirements
Must have
• The images supplied are key to this brief as these are by the author.
• These images can be trimmed to suit your designs but the characters must remain the focus and intact.
• Series Title
• Book Title
• No of book in series
• Author's name
• Company logo (Fenwick & Taverley)
• Spine Design with Series name, Book no of Series, Title, Author, Company Logo
Nice to have
• A font that is appropriate to the Fantasy genre.
• The stories are set in Victorian Britain and there is a battle between good and evil. The images supplied for the front covers are of the good characters.
• To see what the Pale Thistle Annals is all about please visit the facebook page: https://www.exampleface.net/palethistleannals/
• Existing book covers are shown on this page both in posts and the fb store.

```html
<!DOCTYPE html>
<html lang="en">
<head>
<meta charset="utf-8">
<title>Pale Thistle Annals – Stag of Hollowmere – Book III</title>
<link href="https://fonts.googleapis.com/css2?family=Cinzel:wght@400;700&family=Quattrocento:wght@400&display=swap" rel="stylesheet">
<style>
  :root {
    --ink: #000000;
    --paper: #ffffff;
    --silver-light: #ececec;
    --silver-mid: #a9a9a9;
    --silver-dark: #5e5e5e;
    --author-grey: #d4d4d4;
    --art-orange: #c8632a;
    --art-teal: #5f8f8c;
    --art-lilac: #8c86b8;
  }
  * { box-sizing: border-box; margin: 0; padding: 0; }
  html, body { width: 1200px; height: 866px; overflow: hidden; background: var(--ink); }
  .cover-spread { position: relative; width: 1200px; height: 866px; background: var(--ink); color: var(--paper); overflow: hidden; }

  .display { font-family: "Cinzel", serif; font-weight: 700; }
  .caps { font-family: "Cinzel", serif; font-weight: 400; }
  .silver {
    background: linear-gradient(180deg, var(--silver-light) 0%, var(--silver-mid) 55%, var(--silver-dark) 100%);
    -webkit-background-clip: text; background-clip: text; color: transparent;
  }

  /* Back cover */
  .back-art {
    position: absolute; left: 142px; top: 46px; width: 320px; height: 246px;
    border-radius: 48% 52% 45% 55% / 50% 48% 52% 50%;
    background: radial-gradient(ellipse at 50% 48%, var(--art-orange) 0%, #7a3a1e 40%, var(--art-lilac) 72%, #2c2a44 100%);
  }
  .back-title {
    position: absolute; left: 60px; width: 460px; top: 298px; text-align: center;
    font-size: 30px; line-height: 36px; color: var(--paper); white-space: nowrap;
  }
  .blurb {
    position: absolute; font-family: "Quattrocento", serif; font-size: 14.2px; line-height: 17.6px;
    text-align: justify; color: var(--paper); hyphens: auto;
  }
  .blurb-one { left: 62px; top: 342px; width: 456px; }
  .blurb-two { left: 58px; top: 563px; width: 458px; }
  .back-author {
    position: absolute; left: 60px; width: 460px; top: 526px; text-align: center;
    font-size: 24px; line-height: 28px; letter-spacing: 2px; color: var(--author-grey); white-space: nowrap;
  }
  .back-imprint {
    position: absolute; left: 186px; width: 200px; top: 772px; text-align: center;
    font-family: "Cinzel", serif; font-size: 20px; line-height: 24px; color: var(--paper);
  }

  /* Spine */
  .spine-text { position: absolute; transform: rotate(-90deg); text-align: center; white-space: nowrap; }
  .spine-title { left: 464px; top: 154px; width: 272px; height: 36px; font-size: 25px; line-height: 36px; }
  .spine-series { left: 488px; top: 428px; width: 224px; height: 64px; font-size: 25px; line-height: 32px; }
  .spine-author { left: 526px; top: 646px; width: 152px; height: 52px; font-size: 25px; line-height: 26px; letter-spacing: 1px; color: var(--author-grey); }
  .spine-book {
    position: absolute; left: 558px; top: 323px; width: 82px; height: 16px;
    background: linear-gradient(90deg, #cfcfcf, #ffffff 50%, #cfcfcf);
    color: var(--ink); font-family: "Cinzel", serif; font-size: 12px; line-height: 16px; text-align: center;
  }
  .spine-imprint {
    position: absolute; left: 556px; width: 88px; top: 776px; text-align: center;
    font-family: "Cinzel", serif; font-size: 30px; line-height: 36px; color: var(--paper);
  }

  /* Front cover */
  .front-series {
    position: absolute; left: 680px; width: 450px; top: 52px; text-align: center;
    font-size: 50px; line-height: 62px; letter-spacing: 1px; white-space: nowrap;
  }
  .front-art {
    position: absolute; left: 732px; top: 200px; width: 344px; height: 404px;
    border-radius: 46% 54% 48% 52% / 44% 46% 54% 56%;
    border: 4px solid #8d8d8d;
    background: radial-gradient(ellipse at 45% 50%, #a9cfc8 0%, var(--art-teal) 40%, #43505a 62%, var(--art-orange) 82%, #7a3210 100%);
  }
  .front-title {
    position: absolute; left: 654px; width: 520px; top: 630px; text-align: center;
    font-size: 46px; line-height: 58px; white-space: nowrap;
  }
  .book-band { position: absolute; left: 792px; top: 706px; width: 228px; height: 48px; }
  .book-band-label {
    position: absolute; left: 0; top: 10px; width: 228px; height: 28px;
    background: linear-gradient(90deg, rgba(255,255,255,0) 0%, #ffffff 22%, #ffffff 78%, rgba(255,255,255,0) 100%);
    color: var(--ink); font-family: "Cinzel", serif; font-size: 24px; line-height: 28px; text-align: center; letter-spacing: 1px;
  }
  .book-band svg { position: absolute; left: 0; top: 0; }
  .front-author {
    position: absolute; left: 660px; width: 500px; top: 768px; text-align: center;
    font-size: 42px; line-height: 50px; letter-spacing: 4px; white-space: nowrap;
  }
</style>
</head>
<body>
<main class="cover-spread">
  <!-- Back cover -->
  <div class="back-art" role="img" aria-label="Illustration: a creature crawling out of a torn scroll, in orange and lilac tones"></div>
  <h2 class="back-title display">Stag of Hollowmere</h2>
  <p class="blurb blurb-one">"Sed ut perspiciatis unde omnis iste natus error sit voluptatem accusantium doloremque laudantium, totam rem aperiam, eaque ipsa quae ab illo inventore veritatis et quasi architecto beatae vitae dicta sunt explicabo. Nemo enim ipsam voluptatem quia voluptas sit aspernatur aut odit aut fugit, sed quia consequuntur magni dolores eos qui ratione voluptatem sequi nesciunt. Neque porro quisquam est, qui dolorem ipsum quia dolor sit amet, consectetur, adipisci velit, sed quia non numquam eius modi tempora incidunt ut labore et dolore magnam aliquam quaerat vo pariatur?"</p>
  <p class="back-author caps">CLIVE MARLOWE</p>
  <p class="blurb blurb-two">"Lorem ipsum dolor sit amet, consectetur adipiscing elit, sed do eiusmod tempor incididunt ut labore et dolore magna aliqua. Ut enim ad minim veniam, quis nostrud exercitation ullamco laboris nisi ut aliquip ex ea commodo consequat. Duis aute irure dolor in reprehenderit in voluptate velit esse cillum dolore eu fugiat nulla pariatur. Excepteur sint occaecat cupidatat non proident, sunt in culpa qui officia deserunt mollit anim id est laborum."</p>
  <p class="back-imprint">Fenwick<br>&amp; Taverley</p>

  <!-- Spine -->
  <p class="spine-text spine-title display">Stag of Hollowmere</p>
  <p class="spine-book">BOOK III</p>
  <p class="spine-text spine-series display">PALE THISTLE<br>ANNALS</p>
  <p class="spine-text spine-author caps">CLIVE<br>MARLOWE</p>
  <p class="spine-imprint">F&amp;T</p>

  <!-- Front cover -->
  <h1 class="front-series display silver">PALE THISTLE<br>ANNALS</h1>
  <div class="front-art" role="img" aria-label="Illustration: a cloaked swordsman and a companion in pale teal light, framed by fiery orange shapes"></div>
  <h2 class="front-title display silver">Stag of Hollowmere</h2>
  <div class="book-band">
    <svg width="228" height="48" viewBox="0 0 228 48" aria-hidden="true">
      <line x1="40" y1="4" x2="188" y2="4" stroke="#bdbdbd" stroke-width="1.2"/>
      <line x1="40" y1="44" x2="188" y2="44" stroke="#bdbdbd" stroke-width="1.2"/>
    </svg>
    <p class="book-band-label">BOOK III</p>
  </div>
  <p class="front-author caps silver">CLIVE MARLOWE</p>
</main>
</body>
</html>
```